Corporate Design für KH Lahnfeld-Rosenau
Zielgruppe
Beratung (Sucht- und Drogenberatung, Sozialberatung, Psychologische Beratung etc.), Hilfen für Menschen in sozialen und/oder finanziellen Notlagen, vgl. www.kh-lahnfeld-rosenau.de
Aufgabenstellung
Verwendung der Bildmarke Fürsorga (Schriftzug mit Sternbogen, Sternbogen, vgl. Dateien), Verwendung der Farben im Firmennamen: Cyan (CMYK 100/0/0/0, RGB 0/155/220), Violett (CMYK 80/100/0/0, RGB 85/18/133), Schrifttyp für "Fürsorgliches Haus": Helvetica Neue LT Std (55 Roman, 75 Bold od. 95 Black), für Visitenkarten und Briefpapier Platz für Infos vgl. Anhang alte Mustervisitenkarte und alter Musterbrief, Visitenkarten und Briefe sollen individuell an die Mitarbeiter anpassbar sein; Möglichkeit zur Kennzeichnung der Fachbereiche (3 Fachbereiche) auf den Visitenkarten durch farbiges Element o.ä.

```html
<!DOCTYPE html>
<html lang="de">
<head>
<meta charset="utf-8">
<title>Fürsorgliches Haus – Geschäftsausstattung</title>
<link rel="stylesheet" href="https://fonts.googleapis.com/css2?family=Arimo:wght@400;700&display=swap">
<style>
  :root {
    --cyan: #1b9bdc;
    --violet: #5a2e91;
    --text-grey: #6b6b6b;
    --paper: #ffffff;
    --backdrop: #e8e5e2;
    --watermark: #e8f0fa;
  }
  * { box-sizing: border-box; margin: 0; padding: 0; }
  html, body { width: 1200px; height: 1189px; overflow: hidden; }
  body {
    position: relative;
    background: var(--backdrop);
    font-family: "Arimo", Arial, sans-serif;
    color: var(--text-grey);
  }
  .sheet { position: absolute; background: var(--paper); overflow: hidden; }

  /* brand name block */
  .brand { position: absolute; display: flex; align-items: center; gap: 6px; color: var(--cyan); font-weight: 700; }
  .brand-square { background: var(--cyan); flex: none; }
  .brand-name { line-height: 1.05; }

  /* letterhead */
  .letterhead { left: 103px; top: 198px; width: 588px; height: 831px; }
  .letterhead .brand { left: 343px; top: 43px; }
  .letterhead .brand-square { width: 42px; height: 42px; }
  .letterhead .brand-name { font-size: 15px; }
  .letter-block { position: absolute; left: 38px; font-size: 9.3px; line-height: 11.4px; }
  .return-line { top: 150px; font-size: 6.4px; }
  .recipient { top: 166px; }
  .subject { top: 222px; }
  .salutation { top: 257px; }
  .body-copy { top: 279px; width: 410px; position: absolute; z-index: 1; }
  .closing { top: 630px; }
  .signature { top: 664px; }
  .watermark { position: absolute; left: 312px; top: 527px; width: 218px; height: 217px; background: var(--watermark); }
  .letter-footer { position: absolute; top: 784px; left: 0; width: 100%; font-size: 6.6px; line-height: 8.2px; color: var(--cyan); }
  .letter-footer div { position: absolute; top: 0; }
  .foot-address { left: 38px; }
  .foot-phone { left: 160px; }
  .foot-web { left: 261px; }
  .foot-bank { left: 348px; }
  .band { position: absolute; left: 0; bottom: 0; width: 100%; background: var(--violet); }
  .letterhead .band { height: 7px; }

  /* business card front */
  .card-front { left: 758px; top: 202px; width: 363px; height: 226px; }
  .card-front .brand { left: 53px; top: 38px; }
  .card-front .brand-square { width: 41px; height: 41px; }
  .card-front .brand-name { font-size: 14.5px; }
  .card-front .band { height: 4px; }
  .card-col { position: absolute; top: 143px; font-size: 11px; line-height: 14px; color: var(--cyan); }
  .card-person { left: 59px; }
  .card-person .name { color: var(--violet); margin-bottom: 14px; }
  .card-contact { left: 194px; }

  /* card backs */
  .card-back-violet { left: 759px; top: 507px; width: 364px; height: 228px; }
  .card-back-cyan { left: 762px; top: 802px; width: 364px; height: 228px; background: var(--cyan); }
  .back-mark { position: absolute; left: 112px; top: 38px; width: 151px; height: 151px; }
  .card-back-violet .back-mark { background: var(--violet); }
  .card-back-cyan .back-mark { background: var(--paper); }
</style>
</head>
<body>

<section class="sheet letterhead">
  <div class="brand">
    <span class="brand-square"></span>
    <span class="brand-name">Fürsorgliches Haus<br>Lahnfeld-Rosenau</span>
  </div>

  <p class="letter-block return-line">Max Mustermann Beispielstraße 38 12345 Beispielort</p>
  <p class="letter-block recipient">Beispielfirma GmbH<br>Firmenstraße 12<br>12345 Firmenort</p>
  <p class="letter-block subject">Betreffzeile</p>
  <p class="letter-block salutation">Sehr geehrte Damen und Herren,</p>

  <div class="watermark"></div>

  <p class="letter-block body-copy">Lorem ipsum dolor sit amet, consetetur sadipscing elitr, sed diam nonumy eirmod tempor invidunt ut labore et dolore magna aliquyam erat, sed diam voluptua. At vero eos et accusam et justo duo dolores et ea rebum. Stet clita kasd gubergren, no sea takimata sanctus est Lorem ipsum dolor sit amet. Lorem ipsum dolor sit amet, consetetur sadipscing elitr, sed diam nonumy eirmod tempor invidunt ut labore et dolore magna aliquyam erat, sed diam voluptua. At vero eos et accusam et justo duo dolores et ea rebum. Stet clita kasd gubergren, no sea takimata sanctus est Lorem ipsum dolor sit amet. Lorem ipsum dolor sit amet, consetetur sadipscing elitr, sed diam nonumy eirmod tempor invidunt ut labore et dolore magna aliquyam erat, sed diam voluptua. At vero eos et accusam et justo duo dolores et ea rebum. Stet clita kasd gubergren, no sea takimata sanctus est Lorem ipsum dolor sit amet.<br>Duis autem vel eum iriure dolor in hendrerit in vulputate velit esse molestie consequat, vel illum dolore eu feugiat nulla facilisis at vero eros et accumsan et iusto odio dignissim qui blandit praesent luptatum zzril delenit augue duis dolore te feugait nulla facilisi. Lorem ipsum dolor sit amet, consectetuer adipiscing elit, sed diam nonummy nibh euismod tincidunt ut laoreet dolore magna aliquam erat volutpat.<br>Ut wisi enim ad minim veniam, quis nostrud exerci tation ullamcorper suscipit lobortis nisl ut aliquip ex ea commodo consequat. Duis autem vel eum iriure dolor in hendrerit in vulputate velit esse molestie consequat, vel illum dolore eu feugiat nulla facilisis at vero eros et accumsan et iusto odio dignissim qui blandit praesent luptatum zzril delenit augue duis dolore te feugait nulla facilisi.<br>At vero eos et accusam et justo duo dolores et ea rebum. Stet clita kasd gubergren, no sea takimata sanctus est Lorem ipsum dolor sit amet. Lorem ipsum dolor sit amet, consetetur sadipscing elitr, sed diam nonumy eirmod tempor invidunt ut labore et dolore magna aliquyam erat, sed diam voluptua. At vero eos et accusam et justo duo dolores et ea rebum. Stet clita kasd gubergren, no sea takimata sanctus est Lorem ipsum dolor sit amet. Lorem ipsum dolor sit amet, consetetur sadipscing elitr, At accusam aliquyam diam diam dolore dolores duo eirmod eos erat, et nonumy sed tempor et et invidunt justo labore Stet clita ea et gubergren, kasd magna no rebum. sanctus sea sed takimata ut vero voluptua. est Lorem ipsum dolor sit amet. Lorem ipsum dolor sit amet, consetetur</p>

  <p class="letter-block closing">Mit freundlichen Grüßen</p>
  <p class="letter-block signature">Max Mustermann<br>Beispielort, 31. Juli 2014</p>

  <footer class="letter-footer">
    <div class="foot-address">Fürsorgliches Haus<br>Lahnfeld-Rosenau<br>Musterstraße 1<br>D-12345 Musterstadt</div>
    <div class="foot-phone">Tel.: + 49 (0)1234 5678<br>Fax: + 49 (0)1234 56790</div>
    <div class="foot-web">info@lahnfeld-haus.de<br>www.lahnfeld-haus.de</div>
    <div class="foot-bank">Bankinstitut<br>IBAN123456789123456</div>
  </footer>
  <div class="band"></div>
</section>

<section class="sheet card-front">
  <div class="brand">
    <span class="brand-square"></span>
    <span class="brand-name">Fürsorgliches Haus<br>Lahnfeld-Rosenau</span>
  </div>
  <div class="card-col card-person">
    <p class="name">Max Mustermann</p>
    <p>Musterstraße 1<br>D-12345 Musterstadt</p>
  </div>
  <div class="card-col card-contact">
    <p>Tel&nbsp; + 49 (0)1234 5678<br>Fax + 49 (0)1234 56790<br>info@lahnfeld-haus.de<br>www.lahnfeld-haus.de</p>
  </div>
  <div class="band"></div>
</section>

<section class="sheet card-back-violet">
  <div class="back-mark"></div>
</section>

<section class="sheet card-back-cyan">
  <div class="back-mark"></div>
</section>

</body>
</html>
```